Tariq Goldsmiths Stationary Contest

Pakistan’s largest Jewellery, Diamond and luxury watches store requires professional stationery. We have a long list of are trusted clients since 1959, our third generation has successfully maintained and sustained the legacy and excellence in the sector.

We require stationery template as part of this contest. The stationery can be double sided.

We prefer a design that makes use of some of the premium business stationery printing options, such as foil stamping, embossing/debossing, painted edges, spot UV etc (doesn't have to use all these options, only what you feel works, but we are looking for a design that stands out and is memorable and these nice touches have that effect.)

We want an eye catching, innovative, high end professional looking stationery for an out of box design that blends well with our new logo (attached). We want the design to be an out of box solution, you may use any element to compliment the logo. You may consider incorporating watermark etc, highlighting our products (Gold and Diamond Jewellery in addition to Luxury watches)

Company details are as follows;

Company name: Tariq Goldsmiths
Contact Person: Farhan Qureshi
Designation: Business Development Consultant
Mobile: +92 333 815 6042
Email: farhanqureshi@mailvale.com
Website: www.tariqgoldsmiths.com

Target Market(s)

Matrimonial, Elite & Businesses class, Upmarket

Font styles to use
Other font styles liked:
• Designers choice

Colors

Designer to choose colors to be used in the design.

Requirements
Must have
• Look and feel: Upmarket, innovative, Modern, Professional, graceful, Elegant, designer stuff.
Nice to have
• Unique design

```html
<!DOCTYPE html>
<html lang="en">
<head>
<meta charset="utf-8">
<title>Tariq Goldsmiths – Business Card</title>
<link rel="stylesheet" href="https://fonts.googleapis.com/css2?family=Mulish:wght@400;700&display=swap">
<style>
  :root {
    --backdrop: #e4e4e4;
    --card: #d9d9d9;
    --gold: #e2a628;
    --ink: #555658;
    --emboss-light: #ececec;
    --emboss-mid: #d3d3d3;
  }
  * { margin: 0; padding: 0; box-sizing: border-box; }
  html, body {
    width: 1200px;
    height: 1000px;
    overflow: hidden;
    background: var(--backdrop);
    font-family: "Mulish", sans-serif;
  }
  .canvas { position: relative; width: 1200px; height: 1000px; }
  .card {
    position: absolute;
    left: 264px;
    width: 648px;
    height: 370px;
    background: var(--card);
  }
  .card--front { top: 112px; }
  .card--back { top: 518px; }

  .brand-name {
    position: absolute;
    color: var(--gold);
    font-weight: 700;
    font-size: 19px;
    letter-spacing: 0.06em;
    text-transform: uppercase;
    white-space: nowrap;
  }
  .card--front .brand-name { left: 36px; top: 92px; }
  .card--back .brand-name { right: 38px; top: 240px; }

  .contact-name {
    position: absolute; left: 36px; top: 180px;
    color: var(--gold); font-size: 17px; font-weight: 400;
  }
  .contact-role {
    position: absolute; left: 36px; top: 205px;
    color: var(--ink); font-size: 14.5px;
  }
  .divider {
    position: absolute; left: 36px; top: 241px;
    width: 18px; height: 2px; background: var(--gold);
  }
  .details {
    position: absolute; left: 36px; top: 258px;
    list-style: none; font-size: 14.5px; line-height: 23px; color: var(--ink);
  }
  .details .label { color: var(--gold); }

  .emblem-area {
    position: absolute;
    width: 260px; height: 260px;
    border-radius: 50%;
    background: radial-gradient(circle at 40% 35%, var(--emboss-light), var(--emboss-mid) 75%);
  }
  .card--front .emblem-area { left: 351px; top: 63px; }
  .card--back .emblem-area { left: 36px; top: 50px; }
</style>
</head>
<body>
<main class="canvas">
  <section class="card card--front">
    <div class="brand-name">Tariq Goldsmiths</div>
    <div class="contact-name">Farhan Qureshi</div>
    <div class="contact-role">Business Development Consultant</div>
    <div class="divider"></div>
    <ul class="details">
      <li><span class="label">Cell:</span> +92 333 815 6042</li>
      <li><span class="label">Email:</span> farhanqureshi@mailvale.com</li>
      <li><span class="label">Web:</span> www.tariqgoldsmiths.com</li>
    </ul>
    <div class="emblem-area" role="img" aria-label="Embossed circular knotwork ornament"></div>
  </section>

  <section class="card card--back">
    <div class="emblem-area" role="img" aria-label="Embossed circular knotwork ornament"></div>
    <div class="brand-name">Tariq Goldsmiths</div>
  </section>
</main>
</body>
</html>
```